Short Line Railroad website - small company simple homepage

We are looking for someone to design a webpage/home page for our railroad. Doesn't have to be fancy, just basic contact info and links to our regional partners and government agencies. We don't do any online sales but would like a web presence that makes us look professional. We have a logo, and some pictures, but are open to purchasing pictures or other graphical elements to enhance this site. We would like links to our partners websites and emergency information. I don't know how many pages this will take??

Target Market(s)

The website is for our existing customers and their partners, potential new rail customers, regional partners like Ports or Economic Development Agencies, and government regulators. We also need emergency contact info and instructions for the general public.

Industry/Entity Type

It Company

Coding

Coded - Design and coding required

Number of Pages Required

2 page

Font styles to use
Sans Serif

Requirements
Must have
• Our logo - map of railroad and area - some photos - contact info - links to designated partners - emergency contact info and emergency instructions.
• Partners include Harlow County Washington
• Port of Elmstead (Washington)
• MVBTA
• City of Pinecrest Hollow
• National Trackway Bureau
• QBO
• HPMRA
• will add more when I have time
Nice to have
• It would be nice to mostly use our company colors - red, black, and white.
• Just a very professional looking website, with the option of making changes in house in the future.
Should not have
• No ads

```html
<!DOCTYPE html>
<html lang="en">
<head>
<meta charset="utf-8">
<title>Harbor Valley Junction Railroad</title>
<link href="https://fonts.googleapis.com/css2?family=Lato:wght@400;700;900&display=swap" rel="stylesheet">
<style>
:root{
  --red:#d42a1e;
  --red-dark:#a81c13;
  --black:#0b0b0b;
  --charcoal:#1c1c1c;
  --white:#ffffff;
  --grey:#5a5a5a;
  --light:#eeeeee;
  --blue:#1f6c97;
  --field:#3a3a3a;
}
*{box-sizing:border-box;margin:0;padding:0}
html,body{width:1200px;height:2304px;overflow:hidden;background:var(--white);font-family:'Lato',Arial,sans-serif;color:var(--charcoal)}
.page{width:1200px;height:2304px;position:relative}

/* header */
.site-header{height:152px;background:var(--black);display:flex;align-items:center;justify-content:space-between;padding:0 40px}
.brand{display:flex;align-items:center;gap:14px}
.brand-square{width:64px;height:64px;background:var(--red)}
.brand-name{color:var(--red);font-weight:900;font-size:34px;line-height:1.05;width:330px}
.emergency-contact{color:var(--white);text-align:left}
.emergency-contact .label{font-size:17px;letter-spacing:.5px}
.emergency-contact .phone{display:flex;align-items:center;gap:10px;font-size:34px;font-weight:700;margin-top:4px}

/* nav */
.main-nav{height:40px;background:var(--red);display:flex;padding:0 40px;justify-content:space-between;align-items:stretch}
.main-nav a{color:var(--white);text-decoration:none;font-size:16px;font-weight:700;display:flex;align-items:center;padding:0 24px}
.main-nav a.active{background:var(--white);color:var(--red)}

/* hero */
.hero{position:relative;height:588px}
.hero-photo{position:absolute;inset:0;background:linear-gradient(180deg,#cfd7c9 0%,#9aa88c 35%,#5f5a44 70%,#3c3226 100%)}
.hero-callout{position:absolute;right:70px;top:70px;width:300px;background:rgba(20,20,20,.78);text-align:center;padding:22px 20px}
.hero-callout h2{color:var(--red);font-size:30px;font-weight:900;line-height:1}
.hero-callout p{color:var(--red);font-size:18px;font-weight:700;margin-top:2px;letter-spacing:.5px}
.btn-outline{display:block;margin:18px auto 0;border:2px solid var(--white);color:var(--white);font-size:24px;font-weight:700;padding:10px 0;width:210px;letter-spacing:.5px}
.btn-red-small{position:absolute;right:100px;top:292px;background:var(--red);color:var(--white);font-size:14px;font-weight:700;padding:7px 26px;border:1px solid var(--white)}
.hero-band{position:absolute;left:0;right:0;bottom:0;height:262px;background:rgba(200,40,24,.82);text-align:center;color:var(--white);padding:30px 140px 0}
.hero-band h1{font-size:34px;font-weight:400}
.hero-band p{font-size:17px;line-height:1.4;margin-top:10px}
.btn-blue{display:inline-block;background:var(--blue);color:var(--white);font-weight:700;font-size:18px;padding:10px 36px;margin-top:18px}

/* partners */
.partners{height:292px;background:var(--black);text-align:center;padding-top:40px;position:relative}
.section-title-red{color:var(--red);font-size:30px;font-weight:400}
.partner-row{display:flex;justify-content:center;gap:22px;margin-top:44px}
.partner-card{width:242px;height:140px;background:var(--white);display:flex;align-items:center;justify-content:center;gap:12px;padding:0 14px}
.partner-badge{width:44px;height:44px;border-radius:50%;background:#4f8a3b;flex:none}
.partner-name{font-size:19px;font-weight:700;color:#263a6b;text-align:left;line-height:1.15}
.carousel-arrow{position:absolute;top:176px;color:var(--white)}
.carousel-arrow.prev{left:30px}.carousel-arrow.next{right:30px}

/* feature rows */
.feature{position:relative;height:328px;display:flex}
.feature-photo{position:absolute;top:0;bottom:0;width:640px}
.route .feature-photo{left:0;background:radial-gradient(circle at 45% 55%,#f0a24c 0%,#8a4a22 25%,#2a1c18 60%,#141018 100%);clip-path:polygon(0 0,85% 0,100% 50%,85% 100%,0 100%)}
.route .feature-text{margin-left:690px;padding-top:40px;width:460px}
.emergency{height:340px}
.emergency .feature-photo{right:0;width:600px;background:linear-gradient(180deg,#3f6b2c 0%,#577f38 40%,#6a6a52 75%,#4a4034 100%);clip-path:polygon(12% 0,100% 0,100% 100%,12% 100%,0 50%)}
.emergency .feature-text{margin-left:60px;padding-top:50px;width:500px}
.feature h3{font-size:30px;font-weight:700;color:var(--charcoal)}
.feature p{font-size:16px;line-height:1.45;color:var(--grey);margin-top:14px}
.btn-red{display:inline-block;background:var(--red);color:var(--white);font-size:16px;font-weight:700;padding:10px 34px;margin-top:22px}
.icon-tile{position:absolute;background:var(--red);color:var(--white);display:flex;flex-direction:column;align-items:center;justify-content:flex-end;font-size:14px;font-weight:700;padding-bottom:10px}
.route .icon-tile{left:24px;top:100px;width:100px;height:118px}
.emergency .icon-tile{right:0;top:176px;width:120px;height:110px}

/* contact */
.contact{height:280px;background:var(--black);text-align:center;padding-top:30px}
.contact h2{color:var(--white);font-size:30px;font-weight:700;letter-spacing:1px}
.contact-form{display:flex;justify-content:center;gap:16px;margin-top:24px}
.form-col{display:flex;flex-direction:column;gap:12px}
.field{width:300px;height:40px;background:var(--field);color:#bbb;font-size:15px;text-align:left;padding:10px 14px}
.field.message{height:104px}
.btn-send{align-self:flex-end;background:var(--black);border:1px solid var(--white);color:var(--white);font-size:15px;font-weight:700;padding:8px 28px}

/* footer */
.site-footer{height:240px;background:var(--white);display:flex;padding:26px 60px 0;gap:60px}
.footer-col h4{color:var(--red);font-size:16px;font-weight:900;margin-bottom:10px}
.footer-col li{list-style:none;font-size:15px;line-height:1.4}
.footer-col p{font-size:14px;line-height:1.4;color:var(--grey);width:250px}
.news-field{width:250px;height:32px;background:var(--field);color:#bbb;font-size:13px;padding:8px 10px;margin-top:10px}
.btn-dark{display:inline-block;background:var(--black);color:var(--white);font-size:13px;font-weight:700;padding:8px 18px;margin-top:10px}
.info-line{display:flex;gap:10px;align-items:flex-start;font-size:14px;margin-bottom:10px;color:var(--charcoal)}
.footer-brand{margin-left:auto;display:flex;align-items:center;gap:10px;align-self:center;margin-top:-20px}
.footer-brand .brand-square{width:50px;height:50px}
.footer-brand .brand-name{font-size:26px;width:230px}
.copyright{height:44px;background:var(--charcoal);color:#aaa;font-size:12px;text-align:center;line-height:44px;letter-spacing:.5px}
</style>
</head>
<body>
<div class="page">

<header class="site-header">
  <div class="brand">
    <div class="brand-square"></div>
    <div class="brand-name">Harbor Valley Junction Railroad</div>
  </div>
  <div class="emergency-contact">
    <div class="label">FOR EMERGENCY, PLEASE CONTACT</div>
    <div class="phone">
      <svg width="32" height="32" viewBox="0 0 24 24"><circle cx="12" cy="12" r="11" fill="none" stroke="#fff" stroke-width="1.6"/><path d="M8.5 6.5l2 2-1.2 1.5c.7 1.5 1.9 2.7 3.4 3.4l1.5-1.2 2 2-1.3 1.7c-3.6-.4-7.2-4-7.6-7.6z" fill="#fff"/></svg>
      1-800-555-0142
    </div>
  </div>
</header>

<nav class="main-nav">
  <a class="active" href="#">HOME</a><a href="#">ABOUT US</a><a href="#">PARTNERS</a><a href="#">ROUTE</a><a href="#">EMERGENCY INSTRUCTIONS</a><a href="#">CONTACT US</a>
</nav>

<section class="hero">
  <div class="hero-photo" role="img" aria-label="Railroad track running through a wooded corridor with overhead line poles"></div>
  <div class="hero-callout">
    <h2>CONNECTING</h2>
    <p>THE PACIFIC NORTHWEST</p>
    <span class="btn-outline">VIEW ROUTE</span>
  </div>
  <span class="btn-red-small">EMERGENCY INSTRUCTIONS</span>
  <div class="hero-band">
    <h1>Welcome to Harbor Valley Junction Railroad</h1>
    <p>Lorem ipsum dolor sit amet, consectetuer adipiscing elit, sed diam nonummy nibh euismod tincidunt ut laoreet dolore magna aliquam erat volutpat. Ut wisi enim ad minim veniam, quis nostrud exerci tation ullamcorper suscipit lobortis nisl ut aliquip ex ea commodo consequat. Duis autem vel eum iriure dolor in hendrerit in vulputate velit esse molestie consequat, vel illum dolore.</p>
    <span class="btn-blue">DISCOVER MORE</span>
  </div>
</section>

<section class="partners">
  <h2 class="section-title-red">Our Partners</h2>
  <svg class="carousel-arrow prev" width="22" height="34" viewBox="0 0 22 34"><path d="M17 3L4 17l13 14" fill="none" stroke="#fff" stroke-width="4"/></svg>
  <div class="partner-row">
    <div class="partner-card"><span class="partner-badge"></span><span class="partner-name">Harlow County Washington</span></div>
    <div class="partner-card"><span class="partner-badge" style="background:#2b5da8"></span><span class="partner-name">Port of Elmstead</span></div>
    <div class="partner-card"><span class="partner-badge" style="background:#8a8f96"></span><span class="partner-name" style="font-size:28px;color:#555d66">MVBTA</span></div>
    <div class="partner-card"><span class="partner-badge" style="background:#2f8a5a"></span><span class="partner-name" style="font-size:26px;color:#2f6a4a">HPMRA</span></div>
  </div>
  <svg class="carousel-arrow next" width="22" height="34" viewBox="0 0 22 34"><path d="M5 3l13 14L5 31" fill="none" stroke="#fff" stroke-width="4"/></svg>
</section>

<section class="feature route">
  <div class="feature-photo" role="img" aria-label="Locomotive headlights on a track at night"></div>
  <div class="icon-tile">
    <svg width="60" height="60" viewBox="0 0 24 24" style="position:absolute;top:14px"><path d="M12 2a6 6 0 0 0-6 6c0 4.5 6 12 6 12s6-7.5 6-12a6 6 0 0 0-6-6z" fill="#fff"/><circle cx="12" cy="8" r="2.3" fill="#d42a1e"/></svg>
    ROUTE
  </div>
  <div class="feature-text">
    <h3>ROUTE</h3>
    <p>Lorem ipsum dolor sit amet, consectetuer adipiscing elit, sed diam nonummy nibh euismod tincidunt ut laoreet dolore magna aliquam erat volutpat. Ut wisi enim ad minim veniam, quis nostrud exerci tation ullamcorper suscipit lobortis nisl ut aliquip ex ea commodo consequat.</p>
    <span class="btn-red">LEARN MORE ON OUR ROUTE</span>
  </div>
</section>

<section class="feature emergency">
  <div class="feature-text">
    <h3>EMERGENCY INSTRUCTIONS</h3>
    <p>Lorem ipsum dolor sit amet, consectetuer adipiscing elit, sed diam nonummy nibh euismod tincidunt ut laoreet dolore magna aliquam erat volutpat. Ut wisi enim ad minim veniam, quis nostrud exerci tation ullamcorper suscipit lobortis nisl ut aliquip ex ea commodo consequat.</p>
    <span class="btn-red">EMERGENCY INSTRUCTIONS</span>
  </div>
  <div class="feature-photo" role="img" aria-label="Railroad track curving through a green forest"></div>
  <div class="icon-tile">
    <svg width="48" height="48" viewBox="0 0 24 24" style="position:absolute;top:14px"><path d="M12 3L2 21h20z" fill="none" stroke="#fff" stroke-width="2"/><rect x="11" y="9" width="2" height="6" fill="#fff"/><rect x="11" y="16.5" width="2" height="2" fill="#fff"/></svg>
    EMERGENCY
  </div>
</section>

<section class="contact">
  <h2>CONTACT US</h2>
  <div class="contact-form">
    <div class="form-col">
      <div class="field">Name</div>
      <div class="field">Email</div>
      <div class="field">Phone</div>
    </div>
    <div class="form-col">
      <div class="field message">Message</div>
      <span class="btn-send">SEND</span>
    </div>
  </div>
</section>

<footer class="site-footer">
  <div class="footer-col">
    <h4>QUICK LINKS</h4>
    <ul><li>HOME</li><li>ABOUT US</li><li>PARTNERS</li><li>ROUTE</li><li>EMERGENCY INSTRUCTIONS</li><li>CONTACT US</li></ul>
  </div>
  <div class="footer-col">
    <h4>NEWSLETTER SIGN UP</h4>
    <p>Stay informed about company news by signing up for our Newsletter</p>
    <div class="news-field">Email</div>
    <span class="btn-dark">SUBSCRIBE</span>
  </div>
  <div class="footer-col">
    <h4>CONTACT INFO</h4>
    <div class="info-line"><svg width="14" height="18" viewBox="0 0 24 30"><path d="M12 1a10 10 0 0 0-10 10c0 7 10 18 10 18s10-11 10-18A10 10 0 0 0 12 1z" fill="#1c1c1c"/><circle cx="12" cy="11" r="3.5" fill="#fff"/></svg><span>1523 Lorem Ipsum Drive<br>Pinecrest Hollow, WA</span></div>
    <div class="info-line"><svg width="16" height="16" viewBox="0 0 24 24"><path d="M5 3l4 4-2 2.5c1.2 2.6 3.4 4.8 6 6L15.5 13l4 4-2.5 3C9.5 19.5 4.5 14.5 4 7z" fill="#1c1c1c"/></svg><span>1-800-555-0142</span></div>
    <div class="info-line"><svg width="16" height="14" viewBox="0 0 24 18"><rect x="1" y="1" width="22" height="16" fill="none" stroke="#1c1c1c" stroke-width="2"/><path d="M1 1l11 9 11-9" fill="none" stroke="#1c1c1c" stroke-width="2"/></svg><span>info@hvjr-rail.example</span></div>
    <div class="info-line" style="color:var(--blue);font-weight:700">Follow us</div>
  </div>
  <div class="footer-brand">
    <div class="brand-square"></div>
    <div class="brand-name">Harbor Valley Junction Railroad</div>
  </div>
</footer>
<div class="copyright">© 2024 HARBOR VALLEY JUNCTION RAILROAD. ALL RIGHTS RESERVED.</div>

</div>
</body>
</html>
```